The Copperwell

We need a APP for our members. this is a Private Bar/Venue. history of the brick building is it was built in1898 and was a gentleman club, oyster house, cigar factory and then law offices before we purchased and are beginning restoration.
the APP must include
1. direct texting to the concierge
2. calendar of events
3. vantor Lock To open the lock, anyone with a code can approach the door, enable their phone's Bluetooth and press the relevant address from the app.
Read more: http://www.evenpostgazette.co.uk/sciencetech/article-4418206/farewell-metal-keys-phone-bolt-opens-front-door-without-anything-in-hand.html#ixzz9kQR2mpaL
4. Menus from various restaurants from our surrounding area
5. member name and member number to give the feel that the app is personalized
6. the members account balance
7. ability to pay their bill with credit card or quid line monthly and automatically.
8. link to züro with its own icon within the app.
9.the ability to reserve the room
Anything else that may of interest for our members that may be relevant that I may not have mentioned since we are new at this...
35 to 60 years of age
Club

```html
<!DOCTYPE html>
<html lang="en">
<head>
<meta charset="utf-8">
<title>The Copperwell – Restaurant Detail</title>
<link rel="stylesheet" href="https://fonts.googleapis.com/css2?family=Montserrat:wght@400;500;600;700&family=Raleway:wght@400;500&display=swap">
<style>
  :root {
    --page-bg: #e3e7ef;
    --header-bg: #ffffff;
    --ink: #1b1b1b;
    --screen-bg: #000000;
    --text: #ffffff;
    --muted: #5a5a5a;
    --copper: #a77c5c;
    --copper-text: #b48a6b;
    --divider: #1c1c1c;
  }
  * { box-sizing: border-box; margin: 0; padding: 0; }
  html, body { width: 800px; height: 1200px; overflow: hidden; }
  body { background: var(--page-bg); font-family: "Raleway", sans-serif; position: relative; }

  .presentation-header {
    position: absolute; left: 0; top: 0; width: 800px; height: 64px;
    background: var(--header-bg);
    display: flex; justify-content: space-between; align-items: center;
    padding: 0 18px;
    font-family: "Montserrat", sans-serif; color: var(--ink);
  }
  .presentation-header .project { font-size: 25px; font-weight: 500; }
  .presentation-header .count { font-size: 17px; font-weight: 500; padding-top: 4px; }

  .screen {
    position: absolute; left: 100px; top: 92px; width: 600px; height: 1067px;
    background: var(--screen-bg); overflow: hidden; color: var(--text);
    box-shadow: 0 4px 14px rgba(0,0,0,0.12);
  }

  .status-bar {
    position: absolute; left: 0; top: 0; width: 100%; height: 30px;
    display: flex; align-items: center; justify-content: space-between;
    padding: 0 10px; font-size: 17px; font-family: "Raleway", sans-serif;
  }
  .status-bar .left, .status-bar .right { display: flex; align-items: center; gap: 6px; }
  .status-bar .time { position: absolute; left: 0; right: 0; text-align: center; }

  .nav-bar { position: absolute; left: 0; top: 30px; width: 100%; height: 72px; }
  .nav-bar .back { position: absolute; left: 30px; top: 14px; }
  .nav-bar .title {
    position: absolute; left: 0; right: 0; top: 22px; text-align: center;
    font-family: "Montserrat", sans-serif; font-size: 22px; letter-spacing: 8px; font-weight: 500;
  }

  .hero {
    position: absolute; left: 0; top: 102px; width: 100%; height: 334px;
    background:
      linear-gradient(180deg, rgba(0,0,0,0) 40%, rgba(0,0,0,0.75) 80%, #000 100%),
      radial-gradient(ellipse at 45% 55%, #8a5a1c 0%, #4a2e10 30%, #1c130a 60%, #0b0805 100%);
  }
  .hero-text { position: absolute; left: 25px; top: 196px; font-family: "Montserrat", sans-serif; }
  .hero-text .kicker { font-size: 19px; line-height: 24px; letter-spacing: 1.6px; font-weight: 500; }
  .hero-text .venue { font-size: 44px; line-height: 56px; font-weight: 600; letter-spacing: 3px; }
  .hero-text .distance { font-size: 24px; line-height: 40px; letter-spacing: 2px; }

  .description {
    position: absolute; left: 25px; top: 440px; width: 550px;
    font-size: 19px; line-height: 32px;
  }

  .actions { position: absolute; left: 24px; top: 568px; display: flex; gap: 19px; }
  .action-button {
    width: 266px; height: 76px; border: 1.5px solid var(--copper);
    display: flex; align-items: center; justify-content: center;
    font-family: "Montserrat", sans-serif; font-size: 20px; font-weight: 600;
    letter-spacing: 1px; color: var(--copper-text);
  }

  .section-title {
    position: absolute; left: 25px; top: 680px;
    font-family: "Montserrat", sans-serif; font-size: 29px; font-weight: 600; letter-spacing: 2px;
  }

  .menu-row { position: absolute; left: 24px; top: 733px; display: flex; gap: 19px; }
  .menu-card { width: 198px; height: 198px; position: relative; flex-shrink: 0; }
  .menu-card .photo { position: absolute; inset: 0; }
  .menu-card .caption {
    position: absolute; left: 0; right: 0; bottom: 0; height: 51px;
    background: rgba(0,0,0,0.55); padding: 8px 9px;
    font-family: "Montserrat", sans-serif;
  }
  .menu-card .name { font-size: 15px; font-weight: 600; letter-spacing: 0.6px; }
  .menu-card .price { font-size: 14px; margin-top: 2px; }
  .photo-spirits { background: linear-gradient(135deg, #4a3220, #2a1a10 60%, #c9c2b0); }
  .photo-tumbler { background: linear-gradient(135deg, #c9ced2, #8f969c 55%, #b07a3a); }
  .photo-pint { background: radial-gradient(ellipse at 45% 50%, #9a3c12, #3a1a0c 60%, #151010); }

  .tab-bar {
    position: absolute; left: 0; top: 990px; width: 100%; height: 77px;
    border-top: 1px solid var(--divider); display: flex;
  }
  .tab {
    flex: 1; display: flex; flex-direction: column; align-items: center; justify-content: flex-end;
    padding-bottom: 9px; gap: 6px; font-family: "Montserrat", sans-serif; font-size: 15px;
    color: var(--muted);
  }
  .tab.is-active { color: var(--text); font-weight: 500; }
</style>
</head>
<body>
  <header class="presentation-header">
    <span class="project">The Copperwell</span>
    <span class="count">5 Screens</span>
  </header>

  <main class="screen">
    <div class="status-bar">
      <div class="left">
        <svg width="56" height="10" viewBox="0 0 56 10" fill="#fff" stroke="#fff"><circle cx="5" cy="5" r="4"/><circle cx="16" cy="5" r="4"/><circle cx="27" cy="5" r="4"/><circle cx="38" cy="5" r="3.5" fill="none"/><circle cx="49" cy="5" r="3.5" fill="none"/></svg>
        <span>Carrier</span>
        <svg width="18" height="14" viewBox="0 0 18 14" fill="none" stroke="#fff" stroke-width="2"><path d="M1 5a12 12 0 0 1 16 0M4 8a7 7 0 0 1 10 0"/><circle cx="9" cy="11.5" r="1.5" fill="#fff" stroke="none"/></svg>
      </div>
      <span class="time">3:24 PM</span>
      <div class="right">
        <span>100%</span>
        <svg width="40" height="16" viewBox="0 0 40 16"><rect x="1" y="1" width="35" height="14" rx="2" fill="none" stroke="#fff"/><rect x="3" y="3" width="31" height="10" fill="#fff"/><rect x="37" y="5" width="2" height="6" fill="#fff"/></svg>
      </div>
    </div>

    <nav class="nav-bar">
      <svg class="back" width="20" height="32" viewBox="0 0 20 32" fill="none" stroke="#fff" stroke-width="3"><path d="M17 2 3 16l14 14"/></svg>
      <div class="title">LA PORTADA</div>
    </nav>

    <div class="hero" role="img" aria-label="Warm-lit bar interior with a long counter and shelves of bottles">
      <div class="hero-text">
        <div class="kicker">Nearby Bar &amp; Restaurants</div>
        <div class="venue">La Portada</div>
        <div class="distance">0.05 mi</div>
      </div>
    </div>

    <p class="description">La Portada is an authentic Mexican Restaurant, Taqueria and Tequila Bar. Mexican, Latin, Central American, Vegetarian Friendly</p>

    <div class="actions">
      <div class="action-button">Reserve The Room</div>
      <div class="action-button">Open The Door</div>
    </div>

    <h2 class="section-title">Menus</h2>

    <div class="menu-row">
      <div class="menu-card">
        <div class="photo photo-spirits" role="img" aria-label="Bottle of whisky lying on a wooden table"></div>
        <div class="caption"><div class="name">Ridgeway Light</div><div class="price">$3</div></div>
      </div>
      <div class="menu-card">
        <div class="photo photo-tumbler" role="img" aria-label="Cocktail with orange peel in a cut-glass tumbler on marble"></div>
        <div class="caption"><div class="name">Harlow Lager</div><div class="price">$3</div></div>
      </div>
      <div class="menu-card">
        <div class="photo photo-pint" role="img" aria-label="Pint of amber beer with foam head"></div>
        <div class="caption"><div class="name">Seasonal</div><div class="price">$5</div></div>
      </div>
    </div>

    <nav class="tab-bar">
      <div class="tab is-active">
        <svg width="34" height="34" viewBox="0 0 34 34" fill="none" stroke="#fff" stroke-width="2"><path d="M2 2h10v7a5 5 0 0 1-10 0zM7 14v18M3 32h8M18 2v9a3 3 0 0 0 6 0V2M21 2v30M30 2c-3 3-3 10 0 12v18"/></svg>
        <span>Restaurants</span>
      </div>
      <div class="tab">
        <svg width="40" height="34" viewBox="0 0 40 34" fill="none" stroke="#5a5a5a" stroke-width="1.8"><path d="M6 28a14 14 0 0 1 28 0zM2 31h36M20 12v-2M20 2v4M8 5l3 3M32 5l-3 3"/><circle cx="20" cy="11" r="1.5"/></svg>
        <span>Concierge</span>
      </div>
      <div class="tab">
        <svg width="34" height="34" viewBox="0 0 34 34" fill="none" stroke="#5a5a5a" stroke-width="1.6"><rect x="2" y="3" width="30" height="29" rx="2"/><path d="M2 10h30M2 17h30M2 24h30M9.5 10v22M17 10v22M24.5 10v22"/></svg>
        <span>Calendar</span>
      </div>
      <div class="tab">
        <svg width="34" height="34" viewBox="0 0 34 34" fill="none" stroke="#5a5a5a" stroke-width="1.8"><circle cx="23" cy="11" r="8"/><circle cx="25" cy="9" r="2"/><path d="M17 16 3 30v3h4v-3h3v-3h3l6-7"/></svg>
        <span>Vantor Locks</span>
      </div>
    </nav>
  </main>
</body>
</html>
```